Business Card Design

We need a business card for a new company in Sydney, Australia. The business supports the tourism industry, predominantly in the IT and systems area. The company focus is to assist business' to streamline their systems and processes, making the back end more efficient with the end goal making them more effective and profitable.

We would like a design that uses the colours red, white and possible black.

Target Market(s)

Tourism companies

Industry/Entity Type

Tourism

Contact Information for Business Card

Morna Kelleway
VantaLoop
Tel: (+61) 0438 716 254
Email: Morna@vantaloop.com.au

Requirements
Nice to have
• Top right corner of the card rounded.

```html
<!DOCTYPE html>
<html lang="en">
<head>
<meta charset="utf-8">
<title>VantaLoop Business Card</title>
<link href="https://fonts.googleapis.com/css2?family=Play:wght@400;700&display=swap" rel="stylesheet">
<style>
  :root {
    --backdrop: #e9e6e2;
    --card-white: #fbfbfa;
    --red-bright: #c8000b;
    --red-deep: #820008;
    --red-brand: #8a0a10;
    --ink-black: #0b0b0b;
    --text-light: #ffffff;
  }
  * { margin: 0; padding: 0; box-sizing: border-box; }
  html, body {
    width: 1200px;
    height: 800px;
    overflow: hidden;
    background: var(--backdrop);
    font-family: "Play", sans-serif;
  }
  .canvas {
    position: relative;
    width: 1200px;
    height: 800px;
  }
  .business-card {
    position: absolute;
    left: 100px;
    top: 100px;
    width: 1000px;
    height: 600px;
    background: var(--card-white);
    overflow: hidden;
    box-shadow: 0 10px 30px rgba(0,0,0,0.18);
  }
  .side-panel {
    position: absolute;
    inset: 0;
    width: 1000px;
    height: 600px;
  }
  .brand {
    position: absolute;
    left: 70px;
    top: 200px;
    display: flex;
    flex-direction: column;
    align-items: flex-start;
    gap: 22px;
  }
  .brand-dot {
    width: 150px;
    height: 150px;
    border-radius: 50%;
    background: var(--red-brand);
  }
  .brand-name {
    font-size: 52px;
    font-weight: 700;
    color: var(--red-brand);
    letter-spacing: 1px;
    white-space: nowrap;
  }
  .identity {
    position: absolute;
    right: 60px;
    top: 70px;
    text-align: right;
    color: var(--text-light);
    font-size: 34px;
    line-height: 1.3;
    letter-spacing: 1px;
    white-space: nowrap;
  }
  .contact {
    position: absolute;
    right: 60px;
    top: 390px;
    color: var(--text-light);
    font-size: 28px;
    line-height: 1.6;
    letter-spacing: 1px;
    white-space: nowrap;
  }
  .contact-label {
    display: inline-block;
    width: 104px;
  }
</style>
</head>
<body>
<div class="canvas">
  <div class="business-card">
    <svg class="side-panel" viewBox="0 0 1000 600" aria-hidden="true">
      <defs>
        <linearGradient id="panelFill" x1="1" y1="0" x2="0" y2="1">
          <stop offset="0" stop-color="var(--red-bright)"/>
          <stop offset="1" stop-color="var(--red-deep)"/>
        </linearGradient>
      </defs>
      <path class="panel-edge" d="M600,0 C520,220 560,380 300,600" fill="none" stroke="var(--ink-black)" stroke-width="12"/>
      <path class="panel-fill" d="M606,0 C526,220 566,380 306,600 L1000,600 L1000,0 Z" fill="url(#panelFill)"/>
    </svg>

    <div class="brand">
      <div class="brand-dot"></div>
      <div class="brand-name">VantaLoop</div>
    </div>

    <div class="identity">
      <div class="person-name">Morna Kelleway</div>
      <div class="company-name">VantaLoop</div>
    </div>

    <div class="contact">
      <div class="contact-line"><span class="contact-label">Phone:</span>(+61) 0438 716 254</div>
      <div class="contact-line"><span class="contact-label">Email:</span>Morna@vantaloop.com.au</div>
    </div>
  </div>
</div>
</body>
</html>
```